HVAC company business card design

We need a business card design for a HVAC company. The design must look professional. Both sides will be used. The total data to be on the business card is
Name
Position
Email
Direct Phone/Moile Phone
Company Contacts /Address, Phone, Fax, web)
All data will be submit once the design is confirmed. For generic purposes use;
Emre Toksoy
Managing Director
+902324815263 (Mobile)
4712 Sokak No: 9 KBSE Yenikent IZMIR TURKEY
Tel: +902324815263 Fax : +902324815269
www.luvon.com.tr

Target Market(s)

HVAC

Industry/Entity Type

Business

Contact Information for Business Card

The total data to be on the business card is
Name
Position
Email
Direct Phone/Moile Phone
Emre Toksoy
Managing Director
+902324815263 (Mobile)
www.luvon.com.tr
The BC will use both sides of the card. The front will include the full logo and the details for the business card holder. The business card can be divided into vertical/horizontal or to a special shape. The common data like the company address/phone/fax should be indicated elsewehere. The back can contain some part or the whole logo and must contain the web address.

Font styles to use
Serif
Sans Serif

Colors
0355a3
cfdfed

Requirements
Should not have
• Please be careful with the fonts, it shouldnt be too small or too big and must not interfere with the logo fonts. If you need to use a curvy shape please do not use as the logo is already curvy or use the curves from the logo (if it looks good, otherwise forget it)
• We are not in favor of pictograms, only if they are perfect use them.

```html
<!DOCTYPE html>
<html lang="en">
<head>
<meta charset="utf-8">
<title>Luvon Business Card</title>
<link href="https://fonts.googleapis.com/css2?family=Open+Sans:wght@400;600;700&display=swap" rel="stylesheet">
<style>
  :root {
    --navy: #3e4a67;
    --navy-deep: #333e58;
    --brand-blue: #2f6fd0;
    --brand-blue-soft: #cfdfed;
    --ink: #4a4f5a;
    --paper: #ffffff;
    --backdrop: #e9ecf1;
  }
  html, body {
    margin: 0;
    padding: 0;
    width: 1200px;
    height: 800px;
    overflow: hidden;
    background: var(--backdrop);
    font-family: "Open Sans", sans-serif;
  }
  .canvas {
    position: relative;
    width: 1200px;
    height: 800px;
  }
  .card {
    position: absolute;
    top: 245px;
    width: 540px;
    height: 310px;
    overflow: hidden;
    box-shadow: 0 6px 18px rgba(30, 40, 60, 0.18);
  }

  /* Front */
  .card-front {
    left: 40px;
    background: var(--paper);
  }
  .front-bands {
    position: absolute;
    left: 0;
    bottom: 0;
    width: 540px;
    height: 70px;
  }
  .front-logo {
    position: absolute;
    left: 40px;
    top: 92px;
    display: flex;
    align-items: center;
    gap: 12px;
  }
  .logo-dot {
    width: 40px;
    height: 40px;
    border-radius: 50%;
    background: var(--brand-blue);
  }
  .logo-name {
    font-weight: 700;
    font-size: 40px;
    letter-spacing: 3px;
    color: var(--navy);
    line-height: 1;
  }
  .divider {
    position: absolute;
    left: 290px;
    top: 70px;
    width: 2px;
    height: 135px;
    background: var(--brand-blue);
  }
  .holder {
    position: absolute;
    left: 308px;
    top: 68px;
    color: var(--ink);
    font-size: 12px;
    line-height: 1.35;
  }
  .holder-name {
    margin: 0;
    font-size: 18px;
    font-weight: 600;
    color: var(--brand-blue);
    line-height: 1.2;
  }
  .holder-title {
    margin: 0 0 8px;
    font-size: 12.5px;
  }
  .holder-address {
    margin: 0 0 6px;
    font-style: normal;
  }
  .contact-list {
    list-style: none;
    margin: 0;
    padding: 0;
  }
  .contact-list li {
    display: flex;
    align-items: center;
    gap: 7px;
  }
  .contact-icon {
    width: 11px;
    height: 11px;
    flex: none;
  }
  .front-web {
    position: absolute;
    right: 30px;
    bottom: 13px;
    color: var(--paper);
    font-size: 13px;
    letter-spacing: 0.5px;
  }

  /* Back */
  .card-back {
    left: 620px;
    background: linear-gradient(135deg, var(--navy) 0%, var(--navy-deep) 100%);
  }
  .back-logo {
    position: absolute;
    left: 0;
    right: 0;
    top: 0;
    bottom: 0;
    display: flex;
    align-items: center;
    justify-content: center;
    gap: 22px;
  }
  .back-logo .logo-dot {
    width: 90px;
    height: 90px;
  }
  .back-logo .logo-name {
    font-size: 72px;
    letter-spacing: 5px;
    color: var(--paper);
  }
</style>
</head>
<body>
<main class="canvas">

  <section class="card card-front" aria-label="Business card front">
    <div class="front-logo">
      <span class="logo-dot"></span>
      <span class="logo-name">LUVON</span>
    </div>

    <div class="divider"></div>

    <div class="holder">
      <p class="holder-name">Emre Toksoy</p>
      <p class="holder-title">Managing Director</p>
      <address class="holder-address">4712 Sokak No: 9<br>KBSE Yenikent IZMIR TURKEY</address>
      <ul class="contact-list">
        <li>
          <svg class="contact-icon" viewBox="0 0 12 12" aria-hidden="true"><rect x="3" y="0.5" width="6" height="11" rx="1" fill="none" stroke="#2f6fd0" stroke-width="1.2"/><rect x="4.5" y="9" width="3" height="1" fill="#2f6fd0"/></svg>
          +902324815263
        </li>
        <li>
          <svg class="contact-icon" viewBox="0 0 12 12" aria-hidden="true"><path d="M1 4 Q6 0 11 4 L9.5 5.5 L8 4.5 L4 4.5 L2.5 5.5 Z" fill="#2f6fd0"/><rect x="2.5" y="6" width="7" height="5" rx="1" fill="#2f6fd0"/></svg>
          +902324815263
        </li>
        <li>
          <svg class="contact-icon" viewBox="0 0 12 12" aria-hidden="true"><rect x="3" y="1" width="6" height="4" fill="none" stroke="#2f6fd0" stroke-width="1"/><rect x="1" y="5" width="10" height="6" rx="1" fill="#2f6fd0"/></svg>
          +902324815269
        </li>
      </ul>
    </div>

    <svg class="front-bands" viewBox="0 0 540 70" aria-hidden="true">
      <polygon points="0,22 300,62 300,70 0,70" fill="#2f6fd0"/>
      <polygon points="0,30 300,70 0,70" fill="#cfdfed" opacity="0.35"/>
      <polygon points="330,28 540,28 540,70 300,70 300,45" fill="#3e4a67"/>
    </svg>
    <span class="front-web">www.luvon.com.tr</span>
  </section>

  <section class="card card-back" aria-label="Business card back">
    <div class="back-logo">
      <span class="logo-dot"></span>
      <span class="logo-name">LUVON</span>
    </div>
  </section>

</main>
</body>
</html>
```